" É uma empresa de consultoria e assessoria em engenharia ambiental, que trabalha com assistência técnica a advogados criminais. Também trabalha com licenciamento ambiental "

```html
<!DOCTYPE html>
<html lang="pt-BR">
<head>
<meta charset="utf-8">
<title>Ambria — Bloco de anotações</title>
<link rel="stylesheet" href="https://fonts.googleapis.com/css2?family=Cinzel:wght@500&family=Montserrat:wght@400;500;600&display=swap">
<style>
  :root {
    --backdrop: #a9a9a9;
    --forest: #1f4d47;
    --leaf: #8fc49a;
    --leaf-pale: #d9ecdc;
    --paper: #ffffff;
    --rule: #d4d8d6;
    --ink: #3a4a47;
    --label: #2b2b2b;
    --ring: #e9e9e9;
  }
  * { margin: 0; padding: 0; box-sizing: border-box; }
  html, body { width: 1200px; height: 1200px; overflow: hidden; }
  body {
    background: var(--backdrop);
    font-family: "Montserrat", sans-serif;
    position: relative;
  }
  .sheet-title {
    position: absolute; left: 22px; top: 18px;
    font-size: 20px; font-weight: 500; color: var(--label); letter-spacing: .5px;
  }
  .view-label {
    position: absolute; top: 308px; width: 334px; text-align: center;
    font-size: 16px; color: var(--label); letter-spacing: 1px;
  }
  .notepad { position: absolute; top: 348px; width: 334px; height: 492px; }
  .notepad--cover { left: 235px; background: var(--forest); }
  .notepad--inner { left: 622px; background: var(--paper); overflow: hidden; }
  .label--cover { left: 235px; }
  .label--inner { left: 622px; }

  .spiral { position: absolute; top: -14px; left: 14px; width: 306px; height: 30px; }
  .back-edge {
    position: absolute; bottom: -10px; left: 50px; width: 234px; height: 14px;
    background: var(--leaf); border-radius: 0 0 50% 50% / 0 0 100% 100%; z-index: -1;
  }

  .cover-brand {
    position: absolute; left: 0; right: 0; top: 180px; text-align: center; color: var(--paper);
  }
  .brand-dot {
    display: block; width: 50px; height: 50px; margin: 0 auto 14px;
    border-radius: 50%; background: var(--leaf);
  }
  .brand-name {
    font-family: "Cinzel", serif; font-weight: 500; font-size: 40px; letter-spacing: 2px; line-height: 1;
  }
  .brand-tagline {
    margin-top: 8px; font-size: 11.5px; font-weight: 500; letter-spacing: 1.4px;
    line-height: 1.35; color: var(--leaf);
  }

  .inner-brand {
    position: absolute; top: 40px; left: 0; right: 0;
    display: flex; align-items: center; justify-content: center; gap: 10px; color: var(--forest);
  }
  .inner-brand .brand-dot { width: 36px; height: 36px; margin: 0; }
  .inner-brand .brand-name { font-size: 26px; }
  .inner-brand .brand-tagline { margin-top: 3px; font-size: 6.5px; letter-spacing: .8px; color: var(--ink); }

  .watermark {
    position: absolute; left: 70px; top: 150px; width: 250px; height: 250px;
    border-radius: 50%; background: var(--leaf-pale); opacity: .45;
  }
  .rules { position: absolute; left: 18px; right: 18px; top: 120px; }
  .rules span { display: block; height: 23px; border-bottom: 1.5px solid var(--rule); }

  .contacts {
    position: absolute; left: 60px; right: 30px; top: 438px;
    display: grid; grid-template-columns: 1fr 1fr; row-gap: 8px;
    font-size: 8.5px; color: var(--ink);
  }
  .contacts li { list-style: none; display: flex; align-items: center; gap: 5px; }
  .contacts svg { width: 9px; height: 9px; fill: var(--forest); }
</style>
</head>
<body>
  <h1 class="sheet-title">BLOCO DE ANOTAÇÕES</h1>

  <p class="view-label label--cover">CAPA</p>
  <p class="view-label label--inner">MIOLO</p>

  <section class="notepad notepad--cover">
    <svg class="spiral" viewBox="0 0 306 30" aria-hidden="true">
      <g fill="none" stroke="var(--ring)" stroke-width="2.4">
        <path d="M6 28 V8 a4 4 0 0 1 8 0 V20"/><path d="M31 28 V8 a4 4 0 0 1 8 0 V20"/>
        <path d="M56 28 V8 a4 4 0 0 1 8 0 V20"/><path d="M81 28 V8 a4 4 0 0 1 8 0 V20"/>
        <path d="M106 28 V8 a4 4 0 0 1 8 0 V20"/><path d="M131 28 V8 a4 4 0 0 1 8 0 V20"/>
        <path d="M156 28 V8 a4 4 0 0 1 8 0 V20"/><path d="M181 28 V8 a4 4 0 0 1 8 0 V20"/>
        <path d="M206 28 V8 a4 4 0 0 1 8 0 V20"/><path d="M231 28 V8 a4 4 0 0 1 8 0 V20"/>
        <path d="M256 28 V8 a4 4 0 0 1 8 0 V20"/><path d="M281 28 V8 a4 4 0 0 1 8 0 V20"/>
      </g>
    </svg>
    <div class="cover-brand">
      <span class="brand-dot"></span>
      <div class="brand-name">AMBRIA</div>
      <div class="brand-tagline">CONSULTORIA E ASSESSORIA<br>INTEGRADA</div>
    </div>
    <div class="back-edge"></div>
  </section>

  <section class="notepad notepad--inner">
    <svg class="spiral" viewBox="0 0 306 30" aria-hidden="true">
      <g fill="none" stroke="#555" stroke-width="2.4">
        <path d="M6 28 V8 a4 4 0 0 1 8 0 V20"/><path d="M31 28 V8 a4 4 0 0 1 8 0 V20"/>
        <path d="M56 28 V8 a4 4 0 0 1 8 0 V20"/><path d="M81 28 V8 a4 4 0 0 1 8 0 V20"/>
        <path d="M106 28 V8 a4 4 0 0 1 8 0 V20"/><path d="M131 28 V8 a4 4 0 0 1 8 0 V20"/>
        <path d="M156 28 V8 a4 4 0 0 1 8 0 V20"/><path d="M181 28 V8 a4 4 0 0 1 8 0 V20"/>
        <path d="M206 28 V8 a4 4 0 0 1 8 0 V20"/><path d="M231 28 V8 a4 4 0 0 1 8 0 V20"/>
        <path d="M256 28 V8 a4 4 0 0 1 8 0 V20"/><path d="M281 28 V8 a4 4 0 0 1 8 0 V20"/>
      </g>
    </svg>
    <div class="inner-brand">
      <span class="brand-dot"></span>
      <div>
        <div class="brand-name">AMBRIA</div>
        <div class="brand-tagline">CONSULTORIA E ASSESSORIA INTEGRADA</div>
      </div>
    </div>
    <div class="watermark"></div>
    <div class="rules">
      <span></span><span></span><span></span><span></span><span></span><span></span>
      <span></span><span></span><span></span><span></span><span></span><span></span>
    </div>
    <ul class="contacts">
      <li><svg viewBox="0 0 10 10"><path d="M2 0h2l1 3-1.5 1a6 6 0 0 0 2.5 2.5L7 5l3 1v2a2 2 0 0 1-2 2A8 8 0 0 1 0 2a2 2 0 0 1 2-2z"/></svg>(11) 4000-0000</li>
      <li><svg viewBox="0 0 10 10"><rect x="0" y="2" width="10" height="6" rx="1"/></svg>contato@ambria.eco</li>
      <li><svg viewBox="0 0 10 10"><circle cx="5" cy="5" r="4"/></svg>@ambria.eco</li>
      <li><svg viewBox="0 0 10 10"><circle cx="5" cy="5" r="4"/></svg>www.ambria.eco.br</li>
    </ul>
  </section>
</body>
</html>
```